Corvimo Business Card

Corvimo is a young and energetic software development consultancy. We spend our time on the road working with clients on their sites an meeting new potential customers and employees!

We need a sharp, vibrant and memorable business card that will inspires those that receive it to look after it as it oozes quality and is a nice thing in its own right.

We like bold colours and distinctive design. So show us what you can do.

In terms of information on the card, it would be good to see:

* Our logo (Obviously :) )
* Employee name
* Email
* Website address
* Mobile number
* Full company name (Corvimo ltd)
* Registered company number
* Registered company address

Industry/Entity Type

Software

Requirements
Nice to have
• We are thinking that having a QR Code on the business card could be a good way of adding active marketing. It would be good to see if you are able to merge the kind of element in to your designs!

Maybe something special could be achieved using a visual QR Code like those produced at http://www.pixoranta.example/ ? You have our media so feel free to have a play.

```html
<!DOCTYPE html>
<html lang="en">
<head>
<meta charset="utf-8">
<title>Corvimo Business Card</title>
<link rel="stylesheet" href="https://fonts.googleapis.com/css2?family=Open+Sans:wght@400;600&display=swap">
<style>
  :root {
    --backdrop: #b3b3b3;
    --charcoal: #353535;
    --brand-red: #be1e2d;
    --paper: #ffffff;
    --ink: #2b2b2b;
    --muted: #6a6a6a;
  }
  html, body {
    margin: 0;
    padding: 0;
    width: 927px;
    height: 1200px;
    overflow: hidden;
    background: var(--backdrop);
    font-family: "Open Sans", Verdana, sans-serif;
  }
  .sheet {
    position: relative;
    width: 927px;
    height: 1200px;
  }
  .card-front {
    position: absolute;
    left: 20px; top: 20px;
    width: 881px; height: 571px;
    background: var(--charcoal);
  }
  .card-front .accent-band {
    position: absolute;
    left: 0; top: 525px;
    width: 100%; height: 37px;
    background: var(--brand-red);
  }
  .wordmark {
    position: absolute;
    display: flex;
    align-items: center;
    gap: 20px;
    color: var(--brand-red);
    font-weight: 600;
    letter-spacing: 2px;
    line-height: 1;
  }
  .wordmark .mark-square {
    background: var(--brand-red);
  }
  .card-front .wordmark {
    left: 0; right: 0; top: 196px;
    justify-content: center;
    font-size: 110px;
  }
  .card-front .wordmark .mark-square { width: 70px; height: 70px; }

  .card-back {
    position: absolute;
    left: 20px; top: 606px;
    width: 881px; height: 569px;
    background: var(--paper);
  }
  .brand-panel {
    position: absolute;
    left: 0; top: 0;
    width: 439px; height: 100%;
    background: var(--charcoal);
  }
  .brand-panel .wordmark {
    left: 0; right: 0; top: 270px;
    justify-content: center;
    font-size: 74px;
    gap: 14px;
  }
  .brand-panel .wordmark .mark-square { width: 48px; height: 48px; }

  .icon-rail {
    position: absolute;
    left: 803px; top: 0;
    width: 59px; height: 100%;
    background: var(--brand-red);
  }
  .icon-rail svg {
    position: absolute;
    left: 50%;
    transform: translateX(-50%);
    fill: var(--paper);
  }

  .contact {
    position: absolute;
    right: 97px;
    margin: 0;
    text-align: right;
    color: var(--ink);
    font-size: 25px;
    line-height: 31px;
    letter-spacing: 0.5px;
    white-space: nowrap;
  }
  .contact.name {
    font-size: 38px;
    line-height: 44px;
    letter-spacing: 1.5px;
    top: 78px;
  }
  .contact.company {
    top: 126px;
    font-size: 18px;
    line-height: 24px;
    color: var(--muted);
    letter-spacing: 1px;
  }
  .contact.address { top: 183px; }
  .contact.phone { top: 292px; }
  .contact.mobile { top: 350px; }
  .contact.email { top: 437px; }
  .contact.web { top: 489px; }
  .contact.reg-number {
    top: 533px;
    font-size: 14px;
    line-height: 18px;
    color: var(--muted);
  }
</style>
</head>
<body>
<div class="sheet">
  <section class="card-front">
    <div class="wordmark"><span class="mark-square"></span><span class="wordmark-name">Corvimo</span></div>
    <div class="accent-band"></div>
  </section>

  <section class="card-back">
    <div class="brand-panel">
      <div class="wordmark"><span class="mark-square"></span><span class="wordmark-name">Corvimo</span></div>
    </div>

    <p class="contact name">MARA ELLISON</p>
    <p class="contact company">Corvimo ltd</p>
    <p class="contact address">48 Harrow Lane<br>Bristol, BS1 4QT</p>
    <p class="contact phone">+44-117-000-4821</p>
    <p class="contact mobile">+44-7700-900412</p>
    <p class="contact email">mara@corvimo.example</p>
    <p class="contact web">www.corvimo.example</p>
    <p class="contact reg-number">Registered company no. 08412736</p>

    <div class="icon-rail">
      <svg class="icon-pin" style="top:195px" width="26" height="40" viewBox="0 0 26 40" aria-hidden="true">
        <path d="M13 0C5.8 0 0 5.8 0 13c0 9 13 27 13 27s13-18 13-27C26 5.8 20.2 0 13 0zm0 18a5 5 0 1 1 0-10 5 5 0 0 1 0 10z"/>
      </svg>
      <svg class="icon-phone" style="top:300px" width="36" height="26" viewBox="0 0 36 26" aria-hidden="true">
        <path d="M2 9C2 3 34 3 34 9v3h-8V8c0-2-16-2-16 0v4H2z"/>
        <path d="M9 12h18l5 12H4z"/>
        <circle cx="18" cy="18" r="4" fill="#be1e2d"/>
      </svg>
      <svg class="icon-mobile" style="top:344px" width="22" height="42" viewBox="0 0 22 42" aria-hidden="true">
        <rect x="13" y="0" width="3" height="8"/>
        <rect x="1" y="7" width="20" height="35" rx="3"/>
        <rect x="5" y="11" width="12" height="9" fill="#be1e2d"/>
        <g fill="#be1e2d">
          <rect x="5" y="24" width="3" height="3"/><rect x="10" y="24" width="3" height="3"/><rect x="15" y="24" width="3" height="3"/>
          <rect x="5" y="30" width="3" height="3"/><rect x="10" y="30" width="3" height="3"/><rect x="15" y="30" width="3" height="3"/>
          <rect x="5" y="36" width="3" height="3"/><rect x="10" y="36" width="3" height="3"/><rect x="15" y="36" width="3" height="3"/>
        </g>
      </svg>
      <svg class="icon-mail" style="top:447px" width="34" height="24" viewBox="0 0 34 24" aria-hidden="true">
        <rect x="1" y="1" width="32" height="22" fill="none" stroke="#fff" stroke-width="2"/>
        <path d="M1 1l16 13L33 1M1 23l12-11M33 23L21 12" fill="none" stroke="#fff" stroke-width="2"/>
      </svg>
      <svg class="icon-globe" style="top:497px" width="32" height="32" viewBox="0 0 32 32" aria-hidden="true">
        <g fill="none" stroke="#fff" stroke-width="2">
          <circle cx="16" cy="16" r="14"/>
          <ellipse cx="16" cy="16" rx="6" ry="14"/>
          <path d="M2 16h28M16 2v28M5 8h22M5 24h22"/>
        </g>
      </svg>
    </div>
  </section>
</div>
</body>
</html>
```